Bootstrap site for Cloud Services company

Hi,

First I'd like you to submit you design of the homepage. If you are the winner, I'll get you do design the rest and code it up in HTML, CSS etc using bootstrap.

Why bootstrap? This will probably mean
that you understand the fundamentals of CSS and know how to
make a good-looking website. Also should mean that you can throw
together this site relatively easily so you can focus on the design
work. I'll need some icons and banner style images done.

There's no server-side coding involved, and there's also no content to write, just put placemarker text wherever appropriate. You must be familiar with bootstrap.

Our business sells Varnel Suite for Business and IT support services.

The icon for our business is attached.

Basically I want you to go by the design of this site
http://lnk.example-short.test/kQ7r

However, don't just copy it. I want it to be of a similar layout and
style, but be creative.

I like the simplicity and how it's easy to follow visually.

Just submit the homepage, and if you're successful, I'll get you to
design the rest of the pages for me and code up the pages.

Thanks!

Target Market(s)

We are marketing towards businesses that need their IT managed for them.

Industry/Entity Type

Business

Requirements
Must have
• I like how clean and nice the roboto font is, but it's up to you.

You're welcome to take inspiration from the 'Varnel Pulse' layout and design. Nice use of white space and layout.

Menu headings at the top are as follows:
Support | Deployment | Training | Development | Contact Us |
About

Home page:

In a similar style of the referenced webpage http://lnk.example-short.test/kQ7r, I'd
like a single banner that says "Brisbane's leading Varnel Suite
specialists". In the banner have a computer screen or laptop and a
tablet or smartphone with some 'varnel suite for business' style of
logos coming out of it be creative with some nice design.

Under that, 3 square (or something) icons.
Save Money | Collaborate | Grow
just put some placemarker text in it in a similar fashion to the
reference site.

Just throw some other things in there to fill it up a bit.
Should not have
• http://lnk.example-short.test/kQ7r
I don't want the scrolling banner with the site above, static is fine.

I don't like how when the menu is moused-over, the whole page
moves down.

No stock photos of 'successful business people' or 'very attractive
telephone operator waiting to take your call' :)

```html
<!DOCTYPE html>
<html lang="en">
<head>
<meta charset="utf-8">
<title>Cloudvane – Varnel Suite specialists</title>
<link href="https://fonts.googleapis.com/css2?family=Questrial&family=Open+Sans:wght@400;600;700&display=swap" rel="stylesheet">
<style>
:root{
  --ink:#2b2b2b;
  --body:#444;
  --brand:#1d4fa6;
  --hero-a:#0d3c94;
  --hero-b:#2a66c8;
  --btn-light:#c9d9f2;
  --btn-blue:#1f6fd6;
  --line:#d6d6d6;
  --panel:#f1f1f1;
  --page:#eeeeee;
  --foot:#2e2e2e;
  --foot-deep:#1c1c1c;
  --foot-text:#cfcfcf;
}
*{margin:0;padding:0;box-sizing:border-box}
html,body{width:748px;height:1200px;overflow:hidden}
body{position:relative;background:var(--page);font-family:"Open Sans",sans-serif;color:var(--body)}
.abs{position:absolute}
.topline{left:0;top:0;width:748px;height:5px;background:#333}
.header{left:0;top:5px;width:748px;height:83px;background:#fff}
.logo{left:54px;top:46px;display:flex;align-items:center;gap:6px;font-weight:700;font-size:19px;color:var(--brand)}
.logo i{display:block;width:14px;height:14px;border-radius:50%;background:var(--brand)}
.search{left:574px;top:22px;width:132px;height:18px;border:1px solid #ccc;font-size:7px;color:#999;padding:4px 6px}
.search svg{position:absolute;right:5px;top:3px}
.nav{right:54px;top:62px;display:flex;font-family:"Questrial",sans-serif;font-size:10.5px;color:var(--ink)}
.nav span{padding:0 9px}
.nav span+span{border-left:1px solid #555}
.nav span:last-child{padding-right:0}
.hero{left:0;top:88px;width:748px;height:267px;background:radial-gradient(ellipse at 60% 40%,var(--hero-b),var(--hero-a) 75%)}
.hero-title{left:67px;top:139px;font-family:"Questrial",sans-serif;font-weight:400;font-size:18.5px;line-height:24px;color:#fff}
.hero-sub{left:66px;top:192px;font-family:"Questrial",sans-serif;font-weight:400;font-size:14px;color:#fff}
.hero-text{left:66px;top:216px;width:250px;font-size:7.4px;line-height:13px;color:#e3ecfa}
.hero-visual{left:322px;top:118px;width:370px;height:220px;border-radius:6px;background:radial-gradient(ellipse at 50% 50%,rgba(220,228,240,.35),rgba(120,150,200,.12) 70%,transparent)}
.btn{top:270px;height:28px;font-family:"Questrial",sans-serif;font-size:9px;display:flex;align-items:center;justify-content:center;border-radius:2px}
.btn-dl{left:65px;width:91px;background:var(--btn-light);color:#1d3f7c}
.btn-lm{left:166px;width:91px;background:var(--btn-blue);color:#fff}
.container{left:42px;top:355px;width:664px;height:645px;background:#fff}
.card{border:1px solid var(--line);background:#fff;box-shadow:0 3px 4px rgba(0,0,0,.08)}
.feature{top:366px;width:209px;height:123px;padding:9px 12px}
.feature h3{font-family:"Questrial",sans-serif;font-weight:400;font-size:13px;color:var(--ink);display:flex;align-items:center;gap:8px;height:24px}
.feature p{font-size:7.1px;line-height:13px;margin-top:6px;color:var(--body);letter-spacing:-.1px}
.more{font-family:"Questrial",sans-serif;font-size:8.5px;color:var(--ink);margin-top:4px;display:flex;align-items:center;gap:4px}
.more::after{content:"";border-left:4px solid var(--ink);border-top:3px solid transparent;border-bottom:3px solid transparent}
.mainbox{left:50px;top:513px;width:433px;height:469px;border:1px solid var(--line)}
.sidebox{left:489px;top:513px;width:209px;height:469px;border:1px solid var(--line)}
.sec-title{font-family:"Questrial",sans-serif;font-weight:400;font-size:13px;color:var(--ink)}
.side-title{font-size:11.5px}
.txt{font-size:7.2px;line-height:13px;color:var(--body)}
.bold{font-weight:700;color:var(--ink)}
.divider{height:1px;background:var(--line)}
.news{left:501px;top:552px;width:190px}
.news-item{display:flex;gap:7px;height:70px}
.news-photo{flex:0 0 62px;height:53px}
.news-title{font-size:7.2px;line-height:11.5px;font-weight:700;color:var(--ink);margin-bottom:2px}
.news-date{font-size:7.2px;line-height:12px;color:var(--body);margin-bottom:3px}
.lm{font-size:7.4px;font-weight:700;color:var(--ink)}
.footer{left:0;top:1000px;width:748px;height:164px;background:var(--foot)}
.foot-col{top:1029px;font-size:7.2px;color:var(--foot-text)}
.foot-col h4{font-size:9px;font-weight:600;color:#fff;margin-bottom:9px;letter-spacing:.2px}
.foot-col div{height:17.6px}
.vsep{top:1028px;width:1px;height:108px;background:#444}
.connect{left:518px;top:1026px;font-size:8px;font-style:italic;color:#eee}
.social{top:1044px;width:20px;height:20px;border-radius:50%}
.flogo{left:518px;top:1090px;display:flex;align-items:center;gap:8px;font-weight:700;font-size:21px;color:#fff}
.flogo i{display:block;width:18px;height:18px;border-radius:50%;background:#fff}
.bottom{left:0;top:1164px;width:748px;height:36px;background:var(--foot-deep);font-size:7px;color:#ddd}
.bottom .copy{position:absolute;left:52px;top:14px}
.bottom .links{position:absolute;right:56px;top:14px;display:flex}
.bottom .links span{padding:0 6px}
.bottom .links span+span{border-left:1px solid #999}
.bottom .links span:last-child{padding-right:0}
</style>
</head>
<body>
<div class="abs topline"></div>
<header class="abs header"></header>
<div class="abs logo"><i></i>Cloudvane</div>
<div class="abs search">search here
  <svg width="10" height="10" viewBox="0 0 10 10"><circle cx="4" cy="4" r="3" fill="none" stroke="#777" stroke-width="1.4"/><line x1="6.2" y1="6.2" x2="9" y2="9" stroke="#777" stroke-width="1.6"/></svg>
</div>
<nav class="abs nav"><span>Support</span><span>Deployment</span><span>Training</span><span>Development</span><span>Contact Us</span><span>About</span></nav>

<section class="abs hero"></section>
<h1 class="abs hero-title">Brisbane's leading Varnel Suite<br>specialists</h1>
<h2 class="abs hero-sub">Cloudvane tittle line goes here</h2>
<p class="abs hero-text">Nunc tempus felis vitae urna. Vivamus porttitor, neque at volutpat rutrum, purus nisi eleifend libero, a tempus libero lectus feugiat felis. Morbi diam mauris, viverra in, gravida eu, mattis in, ante.</p>
<div class="abs btn btn-dl">DOWNLOAD APP</div>
<div class="abs btn btn-lm">LEARN MORE</div>
<div class="abs hero-visual" role="img" aria-label="Laptop and smartphone showing Varnel Suite web apps"></div>

<div class="abs container"></div>

<div class="abs card feature" style="left:50px">
  <h3><svg width="28" height="22" viewBox="0 0 28 22"><ellipse cx="13" cy="13" rx="11" ry="7" fill="none" stroke="#333" stroke-width="1.6"/><circle cx="19" cy="3" r="2.5" fill="none" stroke="#333" stroke-width="1.4"/><line x1="7" y1="19" x2="7" y2="22" stroke="#333" stroke-width="2"/><line x1="18" y1="19" x2="18" y2="22" stroke="#333" stroke-width="2"/></svg>Save Money</h3>
  <p>Lorem ipsum dolor sit amet, consectetuer adipiscing elit. Nam cursus. Morbi ut mi. Nullam enim leo, egestas id, condimentum at, laoreet mattis, massa. Sed eleifend nonummy diam.</p>
  <div class="more">Learn More</div>
</div>
<div class="abs card feature" style="left:270px">
  <h3><svg width="28" height="22" viewBox="0 0 28 22"><ellipse cx="14" cy="11" rx="12" ry="8" fill="#333"/><path d="M6 16 L3 21 L11 18z" fill="#333"/></svg>Collaborate</h3>
  <p>Lorem ipsum dolor sit amet, consectetuer adipiscing elit. Nam cursus. Morbi ut mi. Nullam enim leo, egestas id, condimentum at, laoreet mattis, massa. Sed eleifend nonummy diam.</p>
  <div class="more">Learn More</div>
</div>
<div class="abs card feature" style="left:489px">
  <h3><svg width="28" height="22" viewBox="0 0 28 22"><path d="M2 4 Q20 0 25 12 Q22 20 12 17 Q4 12 2 4z" fill="#333"/><path d="M4 5 Q16 10 24 20" stroke="#fff" stroke-width="1" fill="none"/></svg>Grow</h3>
  <p>Lorem ipsum dolor sit amet, consectetuer adipiscing elit. Nam cursus. Morbi ut mi. Nullam enim leo, egestas id, condimentum at, laoreet mattis, massa. Sed eleifend nonummy diam.</p>
  <div class="more">Learn More</div>
</div>

<div class="abs mainbox"></div>
<h3 class="abs sec-title" style="left:65px;top:526px">Little About Our Company</h3>
<div class="abs" role="img" aria-label="Analytics dashboard with charts and a smartphone" style="left:65px;top:554px;width:88px;height:97px;background:linear-gradient(160deg,#dfe9f5,#8fb0d4 60%,#2a2f3a)"></div>
<p class="abs txt" style="left:162px;top:552px;width:306px">Pellentesque habitant morbi tristique senectus et netus et malesuada fames ac turpis egestas. In posuere felis nec tortor. Pellentesque faucibus. Ut accumsan ultricies elit. Maecenas at justo id velit placerat molestie.</p>
<p class="abs txt" style="left:162px;top:595px;width:306px">Donec dictum lectus non odio. Cras a ante vitae enim iaculis aliquam. Mauris nunc quam, venenatis nec, euismod sit amet, egestas placerat, est. Pellentesque habitant morbi tristique senectus et netus et malesuada fames ac turpis egestas. Cras id elit. Integer quis urna. Ut ante enim, dapibus malesuada, fringilla eu, condimentum quis</p>
<div class="abs divider" style="left:51px;top:674px;width:431px"></div>
<h3 class="abs sec-title" style="left:65px;top:690px">Support &amp; Services</h3>
<p class="abs txt bold" style="left:65px;top:713px;width:405px;font-size:7.6px">Mauris vel lacus vitae felis vestibulum volutpat. Etiam est nunc, venenatis in, tristique eu.</p>
<p class="abs txt" style="left:65px;top:730px;width:405px">Cum sociis natoque penatibus et magnis dis parturient montes, nascetur ridiculus mus. In iaculis facilisis massa. Etiam eu urna. Sed porta. Suspendisse quam leo, molestie sed, luctus quis, feugiat in, pede. Fusce tellus. Sed metus augue, convallis et, vehicula ut, pulvinar eu, ante. Integer orci tellus, tristique vitae, consequat nec, porta vel, lectus. Nulla sit amet diam. Duis non nunc. Nulla rhoncus dictum metus.</p>
<div class="abs divider" style="left:51px;top:800px;width:431px"></div>
<h3 class="abs sec-title" style="left:67px;top:809px">Development</h3>
<div class="abs" role="img" aria-label="Presenter beside a display screen" style="left:66px;top:830px;width:185px;height:74px;background:linear-gradient(90deg,#c9ccd1,#e9ecef 45%,#8a9098 75%,#c4c8cc)"></div>
<p class="abs txt bold" style="left:69px;top:913px;font-size:7.6px">Nunc tempus felis vitae urna.</p>
<p class="abs txt" style="left:69px;top:929px;width:185px">Vivamus porttitor, neque at volutpat rutrum, purus nisi eleifend libero, a tempus libero</p>
<p class="abs lm" style="left:67px;top:960px">Learn More</p>
<h3 class="abs sec-title" style="left:275px;top:809px">Our Training</h3>
<div class="abs" role="img" aria-label="Training room with people at computers" style="left:273px;top:830px;width:185px;height:74px;background:linear-gradient(180deg,#dfe6ee,#9fb2c8 60%,#5d6f86)"></div>
<p class="abs txt bold" style="left:276px;top:913px;font-size:7.6px">Nunc tempus felis vitae urna.</p>
<p class="abs txt" style="left:276px;top:929px;width:185px">Vivamus porttitor, neque at volutpat rutrum, purus nisi eleifend libero, a tempus libero</p>
<p class="abs lm" style="left:274px;top:960px">Learn More</p>

<div class="abs sidebox"></div>
<h3 class="abs sec-title side-title" style="left:501px;top:524px">Recent News &amp; Projects</h3>
<div class="abs news">
  <div class="news-item">
    <div class="news-photo" role="img" aria-label="Team joining hands" style="background:linear-gradient(160deg,#7fb0e0,#d9c6b0)"></div>
    <div><p class="news-title">Pellentesque nibh libero, ultricies eu, sagittis non.</p><p class="news-date">Posted on 23rd Oct 2012</p><p class="lm">LEARN MORE</p></div>
  </div>
  <div class="news-item">
    <div class="news-photo" role="img" aria-label="Colleagues at a meeting" style="background:linear-gradient(160deg,#c9ced6,#8a9bb3)"></div>
    <div><p class="news-title">Phasellus felis dolor, scelerisque a tempus</p><p class="news-date">Posted on 23rd Oct 2012</p><p class="lm">LEARN MORE</p></div>
  </div>
  <div class="news-item">
    <div class="news-photo" role="img" aria-label="Support staff at work" style="background:linear-gradient(160deg,#d8d0c6,#8d8f96)"></div>
    <div><p class="news-title">Praesent elementum elit at tellus</p><p class="news-date">Posted on 23rd Oct 2012</p><p class="lm">LEARN MORE</p></div>
  </div>
</div>
<div class="abs" style="left:490px;top:768px;width:207px;height:108px;background:var(--panel)"></div>
<h3 class="abs sec-title side-title" style="left:503px;top:781px">Stay connected</h3>
<p class="abs txt" style="left:503px;top:801px;width:185px">Keep up with your interests and important information while you're on the go.</p>
<p class="abs txt" style="left:503px;top:831px;width:185px">Praesent elementum elit at tellus. Curabitur metus ipsum, luctus eu, malesuada ut, tincidunt</p>
<div class="abs" style="left:490px;top:878px;width:207px;height:103px;background:var(--panel)"></div>
<h3 class="abs sec-title side-title" style="left:502px;top:886px">Varnel Suite</h3>
<p class="abs txt" style="left:502px;top:906px;width:188px">Phasellus felis dolor, scelerisque a, tempus eget, lobortis id, libero. Donec scelerisque leo ac risus. Praesent sit amet est. In dictum, dolor eu dictum porttitor, enim felis viverra</p>

<footer class="abs footer"></footer>
<div class="abs foot-col" style="left:62px"><h4>COMPANY</h4><div>About Our Company</div><div>Why We Are</div><div>Deployment</div><div>Training</div><div>Member Now</div></div>
<div class="abs vsep" style="left:164px"></div>
<div class="abs foot-col" style="left:177px"><h4>OUR SERVICES</h4><div>Development</div><div>Save Money</div><div>Collaborate</div><div>Grow Business</div><div>Partners</div></div>
<div class="abs vsep" style="left:282px"></div>
<div class="abs foot-col" style="left:300px"><h4>SUPPORT</h4><div>FAQ</div><div>Support</div><div>Policy Privacy</div><div>Customers</div><div>In the News</div></div>
<div class="abs vsep" style="left:393px"></div>
<div class="abs foot-col" style="left:407px"><h4>CONTACT</h4><div>Sitemap</div><div>Get Connect</div><div>Term of Use</div><div>Contact Info</div></div>
<div class="abs vsep" style="left:502px"></div>
<p class="abs connect">Get Connected With</p>
<div class="abs social" style="left:520px;background:#3b5998"></div>
<div class="abs social" style="left:548px;background:#2fb5e8"></div>
<div class="abs social" style="left:575px;background:#e4e4e4"></div>
<div class="abs social" style="left:602px;background:#d0d0d0"></div>
<div class="abs social" style="left:629px;background:#f0781e"></div>
<div class="abs flogo"><i></i>Cloudvane</div>
<div class="abs bottom">
  <span class="copy">© 2012 Company Name.  All right reserved.  Term of Use</span>
  <div class="links"><span>Support</span><span>Deployment | Training</span><span>Development</span><span>Contact Us</span><span>About</span></div>
</div>
</body>
</html>
```